USB Stick Gewinnspiel
Zielgruppe
Männer, Technikinteressierte
Aufgabenstellung
Design für ein Gewinnspiel bei dem es 100 USB Sticks, 32 GB (mit die kleinsten USB Sticks der Welt) zu gewinnen gibt.
Menüpunkte: Startseite, Teilnahmebedingungen, Preisdetails, Teilnehmen, Datenschutz.
Es soll eine Intro-Seite auf der der Preis groß heraus gestellt ist gestaltet werden mit den entsprechenden Menüpunkten sowie eine Template-Seite in der wir dann alle notwendigen Inhalte einfügen können. Von der Gestaltung her seid Ihr frei. Klein ist jedoch sexy, daher darf der USB Stick mit einer sexy Dame präsentiert werden die Männerherzen höher schlagen läßt.
Gewinnspiele von uns finden Sie auf www.glueckspfad.de damit Sie sich ein Bild über die bisherigen Gewinnspiele machen können.
WICHTIG: Es soll nur die Eingangsseite und eine Template Seite erstellt werden. Die komplette Programmierung bzw. Füllung mit Inhalten wird von uns gemacht! Für die Templateseite wäre eine Breite von 500 Pixeln oder mehr im Bereich wo wir Inhalte einfügen können wünschenswert.
„Normales altbackenes“ HTML mit Tabellen ohne großen CSS Schnick-Schnack würden wir bevorzugen da es für uns einfacher zum Bearbeiten ist.
Das Gewinnspiel wird später auf einer Subdomain laufen und hat somit keinen Domainnamen den man im Titel darstellen kann oder muss.
Das fertige Layout soll dann als geschnittene HTML Datei mit verlinkten Grafiken geliefert werden.

```html
<!DOCTYPE html>
<html lang="de">
<head>
<meta charset="utf-8">
<title>USB-Stick Gewinnspiel – Preisdetails</title>
<link rel="stylesheet" href="https://fonts.googleapis.com/css2?family=Arimo:wght@400;700&display=swap">
<style>
  :root {
    --page-red: #a8001c;
    --nav-active: #6a0012;
    --nav-text: #ffffff;
    --rule: #e8a0a8;
    --panel: #ffffff;
    --ink: #111111;
    --accent: #b00020;
  }
  * { box-sizing: border-box; margin: 0; padding: 0; }
  html, body {
    width: 1200px; height: 900px; overflow: hidden;
    background: var(--page-red);
    font-family: "Arimo", Arial, sans-serif;
  }
  .page { position: relative; width: 1200px; height: 900px; }

  .main-nav {
    position: absolute; top: 50px; right: 168px;
    font-size: 15px; color: var(--nav-text);
    white-space: nowrap;
  }
  .main-nav a { color: var(--nav-text); text-decoration: none; }
  .main-nav a.is-active { color: var(--nav-active); }
  .main-nav .sep { margin: 0 10px; }

  .nav-rule {
    position: absolute; top: 97px; left: 180px; width: 852px;
    height: 1px; background: var(--rule);
  }

  .hero {
    position: absolute; top: 122px; left: 180px; width: 852px; height: 264px;
    background: var(--panel);
  }
  .hero-visual {
    position: absolute; left: 75px; top: 12px; width: 290px; height: 252px;
    background: linear-gradient(135deg, #d9d9d9 0%, #5a5a5a 45%, #2a2a2a 70%, #b00020 100%);
  }
  .hero-copy {
    position: absolute; left: 457px; top: 50px;
    font-size: 22px; line-height: 24px; color: var(--ink);
  }
  .hero-copy strong { font-weight: 700; }
  .hero-copy .prompt { margin-top: 18px; color: var(--accent); }

  .hero-divider {
    position: absolute; top: 386px; left: 180px; width: 852px; height: 4px;
    background: var(--page-red);
  }

  .content {
    position: absolute; top: 390px; left: 180px; width: 852px; height: 510px;
    background: var(--panel);
    padding: 24px 52px 0 52px;
    font-size: 12px; line-height: 15.8px; color: var(--ink);
    white-space: nowrap;
  }
  .content p { margin-bottom: 15px; }
</style>
</head>
<body>
<div class="page">
  <nav class="main-nav">
    <a href="#">Startseite</a><span class="sep">|</span>
    <a href="#" class="is-active">Preisdetails</a><span class="sep">|</span>
    <a href="#">Datenschutz</a><span class="sep">|</span>
    <a href="#">Teilnahmebedingungen</a><span class="sep">|</span>
    <a href="#">Impressum</a>
  </nav>
  <div class="nav-rule"></div>

  <section class="hero">
    <div class="hero-visual" role="img" aria-label="Frau im grauen Hosenanzug mit Laptop, daneben ein winziger USB-Stick und ein rotes Anhänger-Etikett „1 von 100“"></div>
    <div class="hero-copy">
      <p><strong>Gewinne jetzt...</strong><br>Einen von Hundert<br>USB-Sticks mit<br><strong>32 Gb-Speichervolumen</strong></p>
      <p class="prompt">So einfach gehts, hier sind<br>Deine Preisdetalis:</p>
    </div>
  </section>
  <div class="hero-divider"></div>

  <main class="content">
    <p>Ich bin Blindtext. Von Geburt an. Es hat lange gedauert, bis ich begriffen habe, was es bedeutet, ein blinder Text zu sein:<br>
    Man macht keinen Sinn. Man wirkt hier und da aus dem Zusammenhang gerissen. Oft wird man gar nicht erst gelesen.<br>
    Aber bin ich deshalb ein schlechter Text? Ich weiß, daß ich nie die Chance haben werde im Leuchtblatt zu erscheinen.<br>
    Aber bin ich darum weniger wichtig? Ich bin blind! Aber ich bin gerne Text. Und sollten Sie mich jetzt tatsächlich zu Ende lesen,<br>
    dann habe ich etwas geschafft, was den meisten "normalen" Texten nicht gelingt.</p>

    <p>Weit hinten, hinter den Wortbergen, fern der Länder Vokalien und Konsonantien leben die Blindtexte. Abgeschieden wohnen sie<br>
    in Buchstabhausen an der Küste des Semantik, eines großen Sprachozeans. Ein kleines Bächlein namens Wortquell fließt durch<br>
    ihren Ort und versorgt sie mit den nötigen Regelialien. Es ist ein paradiesmatisches Land, in dem einem gebratene Satzteile in<br>
    den Mund fliegen. Nicht einmal von der allmächtigen Interpunktion werden die Blindtexte beherrscht – ein geradezu<br>
    unorthographisches Leben.</p>

    <p>Eines Tages aber beschloss eine kleine Zeile Blindtext, ihr Name war Lorem Ipsum, hinaus zu gehen in die weite Grammatik.<br>
    Der große Oxmox riet ihr davon ab, da es dort wimmele von bösen Kommata, wilden Fragezeichen und hinterhältigen Semikoli,<br>
    doch das Blindtextchen ließ sich nicht beirren. Es packte seine sieben Versalien, schob sich sein Initial in den Gürtel und machte<br>
    sich auf den Weg.</p>

    <p>Als es die ersten Hügel des Kursivgebirges erklommen hatte, warf es einen letzten Blick zurück auf die Skyline seiner Heimatstadt<br>
    Buchstabhausen, die Headline von Alphabetdorf und die Subline seiner eigenen Straße, der Zeilengasse. Wehmütig lief ihm eine<br>
    rhetorische Frage über die Wange, dann setzte es seinen Weg fort.</p>

    <p>Unterwegs traf es eine Copy. Die Copy warnte das Blindtextchen, da, wo sie herkäme wäre sie zigmal umgeschrieben worden<br>
    und alles, was von ihrem Ursprung noch übrig wäre, sei das Wort »und« und das Blindtextchen solle umkehren und wieder in sein<br>
    eigenes, sicheres Land zurückkehren. Doch alles Gutzureden konnte es nicht überzeugen, und so dauerte es nicht lange, bis ihm<br>
    ein paar heimtückische Werbetexter auflauerten, es mit Longe und Parole betrunken machten und es dann in ihre Agentur schleppten,<br>
    wo sie es für ihre Projekte wieder und wieder missbrauchten. Und wenn es nicht umgeschrieben wurde, dann benutzen sie<br>
    es immernoch.</p>
  </main>
</div>
</body>
</html>
```